Amber Lantern Cafe Business Card

We need a business card design for a new European Cafe. Main menu will be coffee and deserts.

Requirements
Must have
• Logo - 1 of the attached versions
Address - TBA (you can use 487 Morrow Ave Unit 9 for now)
Phone - TBA (you can use 555-238-4176 for now)

```html
<!DOCTYPE html>
<html lang="en">
<head>
<meta charset="utf-8">
<title>Amber Lantern Cafe – Business Card</title>
<link rel="stylesheet" href="https://fonts.googleapis.com/css2?family=Open+Sans:wght@400;600;700&display=swap">
<style>
  :root {
    --canvas: #ffffff;
    --stage: #6f7072;
    --card-dark: #000000;
    --card-dark-glow: #2a2a2a;
    --card-light: #ffffff;
    --ink: #111111;
    --mark-dark: #231f20;
    --on-dark: #ffffff;
  }
  * { margin: 0; padding: 0; box-sizing: border-box; }
  html, body {
    width: 1200px; height: 505px; overflow: hidden;
    background: var(--canvas);
    font-family: "Open Sans", Arial, sans-serif;
  }
  .presentation { position: relative; width: 1200px; height: 505px; }
  .stage {
    position: absolute; left: 0; top: 33px; width: 1200px; height: 434px;
    background: var(--stage);
  }
  .card { position: absolute; width: 528px; height: 305px; overflow: hidden; }

  /* Front */
  .card-front {
    left: 60px; top: 95px;
    background: radial-gradient(circle at 55% 45%, var(--card-dark-glow) 0%, var(--card-dark) 70%);
  }
  .card-front .brand {
    position: absolute; left: 110px; top: 119px;
    display: flex; align-items: center; gap: 16px;
  }
  .card-front .brand-square {
    width: 80px; height: 82px; border-radius: 4px; background: var(--on-dark);
  }
  .card-front .brand-name {
    color: var(--on-dark); font-size: 30px; font-weight: 400; letter-spacing: -0.3px;
  }
  .card-front .web-band {
    position: absolute; left: 0; top: 253px; width: 528px; height: 20px;
    background: var(--card-light);
    color: var(--ink); font-size: 14px; font-weight: 700;
    text-align: center; line-height: 20px;
  }

  /* Back */
  .card-back { left: 612px; top: 98px; background: var(--card-light); }
  .card-back .brand {
    position: absolute; left: 36px; top: 38px;
    display: flex; align-items: center; gap: 12px;
  }
  .card-back .brand-square {
    width: 68px; height: 68px; border-radius: 3px; background: var(--mark-dark);
  }
  .card-back .brand-name {
    color: var(--mark-dark); font-size: 25px; font-weight: 400; letter-spacing: -0.3px;
  }
  .card-back .holder-name {
    position: absolute; right: 18px; top: 127px;
    color: var(--ink); font-size: 17px; font-weight: 400;
  }
  .card-back .divider {
    position: absolute; left: 34px; top: 159px; width: 478px; height: 0;
    border-top: 2px dashed var(--ink);
  }
  .card-back .contact {
    position: absolute; left: 35px; top: 194px;
    list-style: none; color: var(--ink); font-size: 16px; line-height: 22.5px;
  }
  .card-back .contact .web { font-weight: 700; }
</style>
</head>
<body>
<main class="presentation">
  <div class="stage"></div>

  <section class="card card-front" aria-label="Card front">
    <div class="brand">
      <span class="brand-square"></span>
      <span class="brand-name">Amber Lantern Cafe</span>
    </div>
    <p class="web-band">www.AmberLantern.com</p>
  </section>

  <section class="card card-back" aria-label="Card back">
    <div class="brand">
      <span class="brand-square"></span>
      <span class="brand-name">Amber Lantern Cafe</span>
    </div>
    <p class="holder-name">MARCUS HALLORAN</p>
    <div class="divider"></div>
    <ul class="contact">
      <li>487 Morrow Ave Unit 9</li>
      <li>555-238-4176</li>
      <li>marcus@amberlantern.com</li>
      <li class="web">www.AmberLantern.com</li>
    </ul>
  </section>
</main>
</body>
</html>
```